lunch and dinne(al a carte) menus

we are a medium sized licenced club that has taken back the dining in the club
in the western suburbs of sydney working class with a rugby league base
our logo is a wolf kelford hawks

Reason: We have changed the name to Bluegate grill it could be done as Bluegate or Bluegate or Bluegate We need a lunch menu and a seperate dinner menu eg Bluegate grill l u n c h or Bluegate grill d i n n e r

Reason: Weve changed the name

Target Market(s)

young families, working class rugby leagues sporty types

Industry/Entity Type

Club

Requirements
Must have
• user friendly

```html
<!DOCTYPE html>
<html lang="en">
<head>
<meta charset="utf-8">
<title>Bluegate Char Grill – Lunch Menu</title>
<link rel="stylesheet" href="https://fonts.googleapis.com/css2?family=Caladea:wght@400;700&family=Rye&display=swap">
<style>
  :root {
    --wall-dark: #1c1a18;
    --wall-mid: #3a3632;
    --plank-light: #e4c89a;
    --plank-dark: #c9a470;
    --plank-edge: #8a6a40;
    --paper-light: #fbf5dc;
    --paper-mid: #f1e6c0;
    --paper-edge: #d9c795;
    --ink: #6a3713;
    --ink-soft: #5a3518;
    --title-ink: #6b3510;
    --rule: #6a3713;
  }
  * { margin: 0; padding: 0; box-sizing: border-box; }
  html, body { width: 848px; height: 1200px; overflow: hidden; background: var(--wall-dark); }
  .menu-canvas {
    position: relative;
    width: 848px;
    height: 1200px;
    overflow: hidden;
    font-family: "Caladea", "Cambria", Georgia, serif;
    color: var(--ink);
  }
  .wood-wall {
    position: absolute; inset: 0;
    background: linear-gradient(180deg, var(--wall-mid) 0%, var(--wall-dark) 50%, var(--wall-mid) 100%);
  }
  .paper-sheet { position: absolute; left: 0; top: 0; width: 848px; height: 1200px; }
  .plank {
    position: absolute;
    left: 14px; width: 820px;
    background: linear-gradient(180deg, var(--plank-light) 0%, var(--plank-dark) 100%);
    border: 2px solid var(--plank-edge);
    display: flex; align-items: center; justify-content: center;
    overflow: hidden;
  }
  .plank--top { top: 27px; height: 76px; }
  .plank--bottom { top: 1064px; height: 112px; }
  .menu-title {
    font-family: "Rye", serif;
    font-size: 52px;
    letter-spacing: 4px;
    color: var(--title-ink);
    font-weight: 400;
    line-height: 1;
    text-transform: uppercase;
    white-space: nowrap;
  }
  .venue-name {
    font-family: "Rye", serif;
    font-size: 48px;
    letter-spacing: 2px;
    color: var(--title-ink);
    line-height: 1;
    text-transform: uppercase;
    white-space: nowrap;
  }
  .price-head, .dish, .price, .dish-note { position: absolute; }
  .price-head {
    top: 176px; font-weight: 700; font-size: 20px; letter-spacing: 0.3px;
  }
  .price-head--member { left: 532px; }
  .price-head--guest { left: 640px; }
  .dish {
    left: 137px; width: 420px;
    font-weight: 700; font-size: 20px; line-height: 30px;
  }
  .dish-note {
    left: 137px; width: 420px;
    font-size: 16px; line-height: 25px; color: var(--ink-soft);
  }
  .price {
    width: 60px; text-align: center;
    font-weight: 700; font-size: 20px; line-height: 30px;
  }
  .price--member { left: 553px; }
  .price--guest { left: 640px; }
  .section-rule {
    position: absolute; left: 177px; width: 486px; height: 3px;
    background: var(--rule);
  }
</style>
</head>
<body>
<main class="menu-canvas">
  <div class="wood-wall" role="img" aria-label="Dark weathered timber plank wall background"></div>

  <svg class="paper-sheet" viewBox="0 0 848 1200" aria-hidden="true">
    <defs>
      <radialGradient id="paperGlow" cx="50%" cy="48%" r="60%">
        <stop offset="0%" stop-color="#fbf5dc"/>
        <stop offset="70%" stop-color="#f1e6c0"/>
        <stop offset="100%" stop-color="#d9c795"/>
      </radialGradient>
    </defs>
    <path fill="url(#paperGlow)" d="
      M110 168 L170 160 L260 170 L350 158 L450 166 L540 160 L640 168 L720 162 L752 176
      L760 230 L748 270 L790 282 L796 330 L770 360 L776 420 L752 470 L790 498 L800 560
      L770 600 L760 660 L792 690 L790 760 L758 790 L770 850 L750 900 L782 930 L786 990
      L752 1020 L730 1062 L600 1058 L480 1066 L360 1058 L240 1064 L120 1058 L100 1030
      L74 1000 L82 940 L62 900 L70 840 L96 800 L64 760 L60 700 L88 660 L70 610 L50 560
      L64 500 L92 470 L60 420 L56 360 L84 320 L58 282 L62 230 L90 200 Z"/>
  </svg>

  <header class="plank plank--top">
    <h1 class="menu-title">Lunch Menu</h1>
  </header>

  <section class="menu-list" aria-label="Lunch menu items">
    <div class="price-head price-head--member">MEMBER</div>
    <div class="price-head price-head--guest">GUEST</div>

    <div class="dish" style="top:204px">Vegetarian Spring Rolls (4) w/Rice</div>
    <div class="price price--member" style="top:204px">8</div>
    <div class="price price--guest" style="top:204px">10</div>

    <div class="dish" style="top:238px">Club Sandwich w/Chips</div>
    <div class="price price--member" style="top:238px">8</div>
    <div class="price price--guest" style="top:238px">10</div>
    <div class="dish-note" style="top:270px">- chicken, bacon, cheese, tomato, lettuce &amp; mayo</div>

    <div class="dish" style="top:301px">Home Made Quiche w/Chips</div>
    <div class="price price--member" style="top:301px">8</div>
    <div class="price price--guest" style="top:301px">10</div>

    <div class="section-rule" style="top:350px"></div>

    <div class="dish" style="top:373px">T-Bone w/Chips &amp; Salad</div>
    <div class="price price--member" style="top:373px">10</div>
    <div class="price price--guest" style="top:373px">12</div>

    <div class="dish" style="top:408px">Open Hamburger w/the Works &amp; Chips</div>
    <div class="price price--member" style="top:408px">10</div>
    <div class="price price--guest" style="top:408px">12</div>

    <div class="dish" style="top:443px">Cajun Chicken Burger with Chips</div>
    <div class="price price--member" style="top:443px">10</div>
    <div class="price price--guest" style="top:443px">12</div>

    <div class="dish" style="top:477px">Spaghetti Bolognaise</div>
    <div class="price price--member" style="top:477px">10</div>
    <div class="price price--guest" style="top:477px">12</div>

    <div class="dish" style="top:512px">Chicken Caesar Salad</div>
    <div class="price price--member" style="top:512px">10</div>
    <div class="price price--guest" style="top:512px">12</div>

    <div class="dish" style="top:547px">Bangers &amp; Mash</div>
    <div class="price price--member" style="top:547px">10</div>
    <div class="price price--guest" style="top:547px">12</div>
    <div class="dish-note" style="top:578px">-1 thick &amp; 1 thin sausage</div>

    <div class="dish" style="top:609px">Vegetarian Lasagne w/Chips &amp; Salad</div>
    <div class="price price--member" style="top:609px">10</div>
    <div class="price price--guest" style="top:609px">12</div>

    <div class="section-rule" style="top:652px"></div>

    <div class="dish" style="top:680px">Chicken or Veal Schnitzel w/Chips &amp;<br>Salad</div>
    <div class="price price--member" style="top:680px">14</div>
    <div class="price price--guest" style="top:680px">16</div>

    <div class="dish" style="top:746px">Open Steak Sandwich</div>
    <div class="price price--member" style="top:746px">14</div>
    <div class="price price--guest" style="top:746px">16</div>
    <div class="dish-note" style="top:778px">-cheese, pineapple, egg</div>

    <div class="dish" style="top:809px">All Day Breakfast</div>
    <div class="price price--member" style="top:809px">14</div>
    <div class="price price--guest" style="top:809px">16</div>
    <div class="dish-note" style="top:839px">-sausage, egg, bacon, mushrooms, tomato, hash<br>brown &amp; toast</div>

    <div class="dish" style="top:897px">Garlic Prawns with Rice &amp; Salad</div>
    <div class="price price--member" style="top:897px">14</div>
    <div class="price price--guest" style="top:897px">16</div>

    <div class="dish" style="top:932px">Beer Battered Barramundi w/Chips and<br>Salad</div>
    <div class="price price--member" style="top:932px">14</div>
    <div class="price price--guest" style="top:932px">16</div>

    <div class="dish" style="top:997px">Seafood Basket with Chips &amp; Salad</div>
    <div class="price price--member" style="top:997px">14</div>
    <div class="price price--guest" style="top:997px">16</div>
  </section>

  <footer class="plank plank--bottom">
    <p class="venue-name">Bluegate Char Grill</p>
  </footer>
</main>
</body>
</html>
```